Mailer

Harbor Quill Partners, LLC
http://www.harborquillpartners.example/
301-555-0148
YOUR SUCCESS
You have an idea about where you want your business to go.  Need some help getting there? Are  you contemplating a transition to a new Broker Dealer, Producer Group or Custodian,  and/or interested in buying or selling a practice.
SOLUTIONS
Harbor Quill Partners, LLC is a consulting firm dedicated to  helping Finanial Advisors with their short term, and long term business affiliation and transition needs. W e interface with multple independent broker dealers and offer completely objective and unbiased guidance to help Financial Advisors find the perfect independent back office. Our services are free to you.

Industry/Entity Type
Business

```html
<!DOCTYPE html>
<html lang="en">
<head>
<meta charset="utf-8">
<title>Harbor Quill Partners Mailer</title>
<link href="https://fonts.googleapis.com/css2?family=Open+Sans:wght@400;600;700;800&family=Merriweather:wght@400;700&display=swap" rel="stylesheet">
<style>
  :root {
    --navy: #1b2a6b;
    --navy-deep: #0f1a4d;
    --royal: #2947b8;
    --sky: #3d7fd6;
    --sky-light: #8fc2f0;
    --snow: #eef4fb;
    --accent-blue: #1f8fe0;
    --white: #ffffff;
    --ink: #1d2440;
    --paper: #ffffff;
    --stage: #e4e7ee;
    --line: #9aa3b8;
  }
  * { box-sizing: border-box; margin: 0; padding: 0; }
  html, body { width: 876px; height: 1200px; overflow: hidden; }
  body {
    background: var(--stage);
    font-family: "Open Sans", Arial, sans-serif;
    position: relative;
  }
  .card {
    position: absolute;
    left: 20px;
    width: 836px;
    height: 560px;
    background: var(--paper);
    overflow: hidden;
    box-shadow: 0 2px 8px rgba(0,0,0,.18);
  }
  .card--front { top: 20px; }
  .card--back { top: 620px; }

  /* Front */
  .front-photo {
    position: absolute; inset: 0 0 180px 0;
    background: linear-gradient(180deg, #1d5fc2 0%, #3d86dc 45%, #a9cdee 70%, #eef4fb 100%);
  }
  .front-wave { position: absolute; left: 0; top: 300px; width: 836px; height: 120px; }
  .headline {
    position: absolute; left: 36px; top: 26px;
    color: var(--white);
    font-weight: 800; font-size: 58px; line-height: 1.02;
    letter-spacing: -0.5px;
  }
  .tagline {
    position: absolute; left: 40px; top: 160px;
    color: #174fb0; font-weight: 800; font-size: 34px;
  }
  .front-contact { position: absolute; left: 36px; top: 408px; color: var(--ink); }
  .company-name { font-size: 38px; font-weight: 600; color: var(--navy); margin-bottom: 12px; }
  .contact-row { display: flex; align-items: center; gap: 12px; font-size: 22px; margin-bottom: 8px; }
  .contact-row svg { width: 22px; height: 22px; }
  .social { position: absolute; right: 40px; top: 480px; display: flex; gap: 10px; }
  .social span { width: 34px; height: 34px; background: var(--royal); border-radius: 4px; }

  /* Back */
  .back-panel {
    position: absolute; left: 0; top: 0; width: 430px; height: 560px;
    background: linear-gradient(160deg, var(--royal) 0%, var(--navy) 60%, var(--navy-deep) 100%);
  }
  .back-curve { position: absolute; left: 0; top: 0; width: 470px; height: 560px; }
  .section-head {
    position: absolute; left: 0; width: 300px; height: 40px;
    background: var(--white); color: var(--navy);
    font-family: "Merriweather", Georgia, serif; font-weight: 700; font-size: 21px;
    padding: 7px 0 0 26px;
    border-radius: 0 20px 20px 0;
  }
  .section-head--success { top: 22px; }
  .section-head--solutions { top: 204px; }
  .section-body {
    position: absolute; left: 26px; color: var(--white);
    font-family: "Merriweather", Georgia, serif;
    font-size: 14px; line-height: 1.5;
  }
  .section-body--success { top: 74px; width: 380px; }
  .section-body--solutions { top: 256px; width: 250px; font-size: 13.2px; }
  .free-note { font-weight: 700; }
  .inset-photo {
    position: absolute; left: 290px; top: 370px; width: 120px; height: 120px;
    border-radius: 50%; border: 5px solid var(--white);
    background: radial-gradient(circle at 50% 35%, #bfdcf6 0%, #4d8fdc 60%, #1b4fa8 100%);
  }
  .visit { position: absolute; left: 26px; bottom: 20px; color: var(--white); }
  .visit-label { font-family: "Merriweather", Georgia, serif; font-size: 14px; margin-bottom: 2px; }
  .visit-url { font-size: 22px; font-weight: 800; }
  .stamp {
    position: absolute; right: 36px; top: 28px; width: 96px; height: 116px;
    border: 2px dashed var(--line);
  }
  .address-lines { position: absolute; left: 500px; top: 260px; width: 300px; }
  .address-lines span { display: block; height: 1px; background: var(--line); margin-bottom: 52px; }
</style>
</head>
<body>

<section class="card card--front" aria-label="Mailer front">
  <div class="front-photo" role="img" aria-label="Snowboarder jumping against a blue sky above snowy mountain peaks"></div>
  <svg class="front-wave" viewBox="0 0 836 120" preserveAspectRatio="none" aria-hidden="true">
    <path d="M0 40 C220 120 520 -10 836 50 L836 120 L0 120 Z" fill="#1b2a6b"/>
    <path d="M0 70 C240 130 540 20 836 80 L836 120 L0 120 Z" fill="#2947b8"/>
    <path d="M0 92 C260 140 560 50 836 100 L836 120 L0 120 Z" fill="#ffffff"/>
  </svg>
  <h1 class="headline">Some dream<br>of success</h1>
  <p class="tagline">We make it happen</p>

  <div class="front-contact">
    <p class="company-name">Harbor Quill Partners, LLC</p>
    <p class="contact-row">
      <svg viewBox="0 0 24 24" aria-hidden="true"><path fill="#1b2a6b" d="M6.6 10.8a15 15 0 006.6 6.6l2.2-2.2c.3-.3.7-.4 1-.2 1.1.4 2.3.6 3.6.6.6 0 1 .4 1 1V20c0 .6-.4 1-1 1A17 17 0 013 4c0-.6.4-1 1-1h3.5c.6 0 1 .4 1 1 0 1.3.2 2.5.6 3.6.1.3 0 .7-.2 1z"/></svg>
      301-555-0148
    </p>
    <p class="contact-row">
      <svg viewBox="0 0 24 24" aria-hidden="true"><rect x="2" y="5" width="20" height="14" rx="2" fill="#1b2a6b"/><path d="M3 6l9 7 9-7" stroke="#fff" stroke-width="1.6" fill="none"/></svg>
      Dana@harborquillpartners.example
    </p>
  </div>
  <div class="social" aria-hidden="true"><span></span><span></span><span></span></div>
</section>

<section class="card card--back" aria-label="Mailer back">
  <div class="back-panel"></div>
  <svg class="back-curve" viewBox="0 0 470 560" preserveAspectRatio="none" aria-hidden="true">
    <path d="M430 0 C470 180 470 380 430 560 L420 560 C455 380 455 180 420 0 Z" fill="#8fc2f0"/>
  </svg>

  <h2 class="section-head section-head--success">YOUR SUCCESS</h2>
  <p class="section-body section-body--success">You have an idea about where you want your business to go. Need some help getting there? Are you contemplating a transition to a new Broker Dealer, Producer Group or Custodian, and/or interested in buying or selling a practice.</p>

  <h2 class="section-head section-head--solutions">SOLUTIONS</h2>
  <p class="section-body section-body--solutions">Harbor Quill Partners, LLC is a consulting firm dedicated to helping Finanial Advisors with their short term, and long term business affiliation and transition needs. We interface with multple independent broker dealers and offer completely objective and unbiased guidance to help Financial Advisors find the perfect independent back office. <span class="free-note">Our services are free to you.</span></p>

  <div class="inset-photo" role="img" aria-label="Small round photo of a snowboarder mid-jump"></div>

  <div class="visit">
    <p class="visit-label">For more information visit us</p>
    <p class="visit-url">www.harborquillpartners.example</p>
  </div>

  <div class="stamp" aria-hidden="true"></div>
  <div class="address-lines" aria-hidden="true"><span></span><span></span><span></span><span></span></div>
</section>

</body>
</html>
```